Health & Fitness Retreat Homepage Design

We have an existing website at http://www.WillowBendHaven.com.au which we are retaining but wish to have a freshly designed homepage with the existing top navigation bar.
Sample layout is attached, but feel free to use your creativity on layout and colours, always remembering it needs to fit with the wider site design.
Project Delivery:
5 phase slide slow at top of homepage
Full homepage design and associated files
Target Audience:
- Female 80%, Male 20%
- Aged 30 to 50
- Overweight/Obese (so no pictures of thin people)
See attached layout for more information.
Target Market(s)
Target Audience:
- Female 80%, Male 20%
- Aged 30 to 50
Industry/Entity Type
Fitness
Requirements
Must have
- Must have existing top navigation bar as at http://www.WillowBendHaven.com.au and fit with existing interior colours, etc.
Should not have
- No pictures of thin people

```html
<!DOCTYPE html>
<html lang="en">
<head>
<meta charset="utf-8">
<title>WillowBendHaven – Weight Loss Retreats</title>
<link href="https://fonts.googleapis.com/css2?family=Oswald:wght@400;500&display=swap" rel="stylesheet">
<style>
:root{
  --green-head:#4f8d12;
  --green-panel:#67b801;
  --green-dark:#2f5d04;
  --orange:#f5893a;
  --orange-link:#f07f2a;
  --text:#3a3a3a;
  --charcoal:#3b3b3b;
  --charcoal-line:#5a5a5a;
  --grey-band:#e7e8e9;
  --white:#fff;
}
*{margin:0;padding:0;box-sizing:border-box}
html,body{width:819px;height:1200px;overflow:hidden;background:var(--white)}
body{font-family:Arial,Helvetica,sans-serif;color:var(--text)}
.page{position:relative;width:951px;height:1393px;transform:scale(.8612);transform-origin:0 0}
.main{position:absolute;left:75px;top:10px;width:520px}
.section-title{font-family:'Oswald',sans-serif;font-weight:500;color:var(--green-head);font-size:19px;line-height:24px;letter-spacing:.1px}
.ticks{list-style:none;margin:6px 0 0 3px}
.ticks li{position:relative;padding-left:19px;font-size:13px;line-height:20px}
.ticks li svg{position:absolute;left:0;top:6px}
.copy{font-size:13px;line-height:19.5px;margin-top:17px;padding-left:2px}
.links{margin-top:7px;padding-left:1px}
.links a{display:block;font-size:12px;line-height:19px;color:var(--orange-link)}
.cta{display:block;width:316px;height:32px;margin-top:17px;background:var(--orange);color:var(--white);font-size:12px;font-weight:bold;line-height:32px;padding-left:14px}
.cta a{color:#4a2a10;text-decoration:underline}
.gap-lg{margin-top:26px}
.results-card{position:absolute;left:628px;top:26px;width:251px}
.results-card .bar{background:#4a4a4a;color:var(--white);font-family:'Oswald',sans-serif;font-size:16px;text-align:center;height:32px;line-height:32px}
.results-card .body{background:var(--orange);padding:4px 2px 10px 5px}
.photo{height:119px;background:linear-gradient(90deg,#b7865c,#d9c7ad 45%,#8a6f62 75%,#b89a84)}
.results-card ul{list-style:none;margin-top:10px}
.results-card li{color:var(--white);font-size:12px;font-weight:bold;line-height:20px;padding-left:23px;position:relative}
.results-card li::before{content:"";position:absolute;left:10px;top:7px;width:7px;height:7px;border-radius:50%;background:var(--white)}
.results-card .foot{background:#4a4a4a;height:35px;text-align:center;line-height:35px}
.results-card .foot a{color:var(--white);font-weight:bold;font-size:15px}
.benefits{position:absolute;left:628px;top:320px;width:251px;height:585px;background:var(--green-panel);border-radius:2px;padding:14px 12px 0 20px}
.benefits h2{font-family:'Oswald',sans-serif;font-weight:500;color:var(--white);font-size:27px;line-height:32px;letter-spacing:.5px}
.benefits h3{font-family:'Oswald',sans-serif;font-weight:500;color:var(--green-dark);font-size:13.5px;line-height:19px;margin-top:4px}
.benefits ul{list-style:none;margin-top:17px}
.benefits li{position:relative;color:var(--white);font-size:12px;line-height:13.5px;padding-left:22px;margin-bottom:14px}
.benefits li svg{position:absolute;left:2px;top:1px}
.site-footer{position:absolute;left:0;top:1140px;width:951px;height:143px;background:var(--charcoal)}
.site-footer .cols{display:flex;height:49px;border-bottom:1px solid var(--charcoal-line)}
.site-footer h4{position:absolute;top:24px;color:var(--orange);font-size:12.5px;font-weight:bold}
.site-footer ul{position:absolute;top:61px;list-style:none}
.site-footer li{font-size:10px;color:#cfcfcf;line-height:16px;padding-left:14px;position:relative}
.site-footer li svg{position:absolute;left:1px;top:3px}
.seo-band{position:absolute;left:0;top:1283px;width:951px;height:45px;background:var(--grey-band);text-align:center;font-size:9px;line-height:13px;color:#444;padding-top:9px}
.legal{position:absolute;left:0;top:1330px;width:951px;height:63px;background:var(--grey-band);font-size:9px;color:#333}
.legal .left{position:absolute;left:71px;top:18px}
.legal .right{position:absolute;right:74px;top:18px;text-align:right;line-height:11px}
</style>
</head>
<body>
<div class="page">
  <main class="main">
    <h1 class="section-title">The Best Located Weight Loss Camps in Australia</h1>
    <ul class="ticks">
      <li><svg width="11" height="9" viewBox="0 0 11 9"><path d="M1 4.5l3 3L10 1" fill="none" stroke="#3e6fb3" stroke-width="2"/></svg>Stunning Weight Loss Retreats &amp; Weight Loss Camp Locations.</li>
      <li><svg width="11" height="9" viewBox="0 0 11 9"><path d="M1 4.5l3 3L10 1" fill="none" stroke="#3e6fb3" stroke-width="2"/></svg>Comfortable Weight Loss Health Retreats Accommodation.</li>
      <li><svg width="11" height="9" viewBox="0 0 11 9"><path d="M1 4.5l3 3L10 1" fill="none" stroke="#3e6fb3" stroke-width="2"/></svg>Excellent Weight Loss Retreat Facilities.</li>
    </ul>
    <p class="copy">Praesent vestibulum molestie lacus. Aenean ummy hendrerit mauris. Phasellus porta. Fusce suscipit varius mi. Aliquam congue fermentum maris accumsan nulla vel.</p>
    <p class="copy">Praesent vestibulum molestie lacus, aenean ummy hendrerit mauris. Phasellus porta, fusce suscipit varius mi. Aliquam congue fermentum maris accumsan nulla vel, praesent vestibulum molestie lacus, aenean ummy hendrerit mauris. Phasellus port, fusce suscipit varius mi. Aliquam congue fermentum maris accumsan nulla vel.</p>
    <div class="links">
      <a href="#">Central Coast NSW Weight Loss Retreat &amp; Weight Loss Camp &gt;&gt;</a>
      <a href="#">Sydney Weight Loss Retreat &amp; Weight Loss Camp at Blue Mountain, NSW &gt;&gt;</a>
    </div>
    <p class="copy gap-lg">Praesent vestibulum molestie lacus. Aenean ummy hendrerit mauris. Phasellus porta. Fusce suscipit varius mi. Aliquam congue fermentum maris accumsan nulla vel, praesent vestibulum molestie lacus, aenean ummy hendrerit mauris.</p>
    <div class="links"><a href="#">Victoria Weight Loss Retreat Near Melbourne &gt;&gt;</a></div>
    <div class="cta">Call: 1300 555 218 or <a href="#">Request a Brochure &gt;&gt;</a></div>

    <h2 class="section-title" style="margin-top:30px">Life Changing Weight Loss Results that Last</h2>
    <ul class="ticks">
      <li><svg width="11" height="9" viewBox="0 0 11 9"><path d="M1 4.5l3 3L10 1" fill="none" stroke="#3e6fb3" stroke-width="2"/></svg>Praesent vestibulum molestie lacus.</li>
      <li><svg width="11" height="9" viewBox="0 0 11 9"><path d="M1 4.5l3 3L10 1" fill="none" stroke="#3e6fb3" stroke-width="2"/></svg>Aenean ummy hendrerit mauris. Phasellus porta.</li>
      <li><svg width="11" height="9" viewBox="0 0 11 9"><path d="M1 4.5l3 3L10 1" fill="none" stroke="#3e6fb3" stroke-width="2"/></svg>Fusce suscipit varius mi. Aliquam congue fermentum maris accumsan nulla vel.</li>
      <li><svg width="11" height="9" viewBox="0 0 11 9"><path d="M1 4.5l3 3L10 1" fill="none" stroke="#3e6fb3" stroke-width="2"/></svg>Phasellus porta,fusce suscipit varius mi.</li>
    </ul>
    <p class="copy">Praesent vestibulum molestie lacus. Aenean ummy hendrerit mauris. Phasellus porta. Fusce suscipit varius mi. Aliquam congue fermentum maris accumsan nulla vel. Praesent vestibulum molestie lacus, aenean ummy hendrerit mauris. Phasellus porta, fusce suscipit varius mi. Aliquam congue fermentum maris accumsan nulla vel, praesent vestibulum molestie lacus, aenean ummy hendrerit mauris.</p>
    <p class="copy">Phasellus port,fusce suscipit varius mi. Aliquem congue fermentum maris accumsan nulla vel. Praesent vestibulum molestie lacus. Aenean ummy hendrerit mauris. Phasellus porta. Fusce suscipit varius mi. Aliquam congue fermentum maris accumsan nulla vel.</p>
    <p class="copy">Praesent vestibulum molestie lacus, aenean ummy hendrerit mauris. Phasellus porta, fusce suscipit varius mi. Aliquem congue fermentum maris accumsan nulla vel, praesent vestibulum molestie lacus, aenean ummy hendrerit mauris. Praesent vestibulum molestie lacus. Aenean ummy hendrerit mauris. Phasellus porta.</p>
    <p class="copy">Fusce suscipit varius mi. Aliquam congue fermentum maris accumsan nulla vel. Praesent vestibulum molestie lacus, aenean ummy hendrerit mauris. Phasellus porta, fusce suscipit varius mi. Aliquam congue fermentum maris accumsan nulla vel, praesent vestibulum molestie lacus, aenean ummy hendrerit mauris.</p>
    <div class="links" style="margin-top:10px"><a href="#">Read more about Weight Loss Retreat Program here &gt;&gt;</a></div>
    <div class="cta">Call: 1300 555 218 or <a href="#">Request a Brochure &gt;&gt;</a></div>
  </main>

  <aside class="results-card">
    <div class="bar">Real People - Real Results</div>
    <div class="body">
      <div class="photo" role="img" aria-label="Photo of three smiling women of different sizes on a city street"></div>
      <ul>
        <li>100`s of people helped by WillowBend</li>
        <li>People of all ages, shapes, and sizes</li>
        <li>Normal people just like you</li>
      </ul>
    </div>
    <div class="foot"><a href="#">Testimonials and Reviews &gt;&gt;</a></div>
  </aside>

  <aside class="benefits">
    <h2>AMAZING RESULTS</h2>
    <h3>FOR PEOPLE OF ALL AGES, SHAPES,<br>SIZES AND FITNESS LEVEL</h3>
    <ul>
      <li><svg width="10" height="8" viewBox="0 0 10 8"><path d="M1 4l2.5 2.5L9 1" fill="none" stroke="#fff" stroke-width="2"/></svg>Weight loss</li>
      <li><svg width="10" height="8" viewBox="0 0 10 8"><path d="M1 4l2.5 2.5L9 1" fill="none" stroke="#fff" stroke-width="2"/></svg>Fat loss</li>
      <li><svg width="10" height="8" viewBox="0 0 10 8"><path d="M1 4l2.5 2.5L9 1" fill="none" stroke="#fff" stroke-width="2"/></svg>Lose centimetres of your waist, hips, thighs and from all over your body</li>
      <li><svg width="10" height="8" viewBox="0 0 10 8"><path d="M1 4l2.5 2.5L9 1" fill="none" stroke="#fff" stroke-width="2"/></svg>Increased flexibility</li>
      <li><svg width="10" height="8" viewBox="0 0 10 8"><path d="M1 4l2.5 2.5L9 1" fill="none" stroke="#fff" stroke-width="2"/></svg>Improved mobility and agility</li>
      <li><svg width="10" height="8" viewBox="0 0 10 8"><path d="M1 4l2.5 2.5L9 1" fill="none" stroke="#fff" stroke-width="2"/></svg>Transform your skin condition</li>
      <li><svg width="10" height="8" viewBox="0 0 10 8"><path d="M1 4l2.5 2.5L9 1" fill="none" stroke="#fff" stroke-width="2"/></svg>Feel happier</li>
      <li><svg width="10" height="8" viewBox="0 0 10 8"><path d="M1 4l2.5 2.5L9 1" fill="none" stroke="#fff" stroke-width="2"/></svg>Eliminate high blood pressure</li>
      <li><svg width="10" height="8" viewBox="0 0 10 8"><path d="M1 4l2.5 2.5L9 1" fill="none" stroke="#fff" stroke-width="2"/></svg>Eliminate Type 2 Diabetes</li>
      <li><svg width="10" height="8" viewBox="0 0 10 8"><path d="M1 4l2.5 2.5L9 1" fill="none" stroke="#fff" stroke-width="2"/></svg>Reduce cholesterol issues</li>
      <li><svg width="10" height="8" viewBox="0 0 10 8"><path d="M1 4l2.5 2.5L9 1" fill="none" stroke="#fff" stroke-width="2"/></svg>Improve previous injuries</li>
      <li><svg width="10" height="8" viewBox="0 0 10 8"><path d="M1 4l2.5 2.5L9 1" fill="none" stroke="#fff" stroke-width="2"/></svg>Reduce head aches</li>
      <li><svg width="10" height="8" viewBox="0 0 10 8"><path d="M1 4l2.5 2.5L9 1" fill="none" stroke="#fff" stroke-width="2"/></svg>Reduce stress</li>
      <li><svg width="10" height="8" viewBox="0 0 10 8"><path d="M1 4l2.5 2.5L9 1" fill="none" stroke="#fff" stroke-width="2"/></svg>No more anxiety</li>
      <li><svg width="10" height="8" viewBox="0 0 10 8"><path d="M1 4l2.5 2.5L9 1" fill="none" stroke="#fff" stroke-width="2"/></svg>Significant improvements for those suffering depression</li>
    </ul>
  </aside>

  <footer class="site-footer">
    <div class="cols"></div>
    <h4 style="left:89px">The Best Programs</h4>
    <h4 style="left:293px">The Best Locations</h4>
    <h4 style="left:513px">About Us</h4>
    <h4 style="left:715px">FREE Information</h4>
    <ul style="left:87px">
      <li><svg width="6" height="8"><path d="M0 0l6 4-6 4z" fill="#f5893a"/></svg>Weight Loss Retreat</li>
      <li><svg width="6" height="8"><path d="M0 0l6 4-6 4z" fill="#f5893a"/></svg>Fitness Boot Camp</li>
      <li><svg width="6" height="8"><path d="M0 0l6 4-6 4z" fill="#f5893a"/></svg>Home program</li>
    </ul>
    <ul style="left:291px">
      <li><svg width="6" height="8"><path d="M0 0l6 4-6 4z" fill="#f5893a"/></svg>Blue Mountains, NSW</li>
      <li><svg width="6" height="8"><path d="M0 0l6 4-6 4z" fill="#f5893a"/></svg>Central Coast, NSW</li>
      <li><svg width="6" height="8"><path d="M0 0l6 4-6 4z" fill="#f5893a"/></svg>Victoria (Torquay)</li>
    </ul>
    <ul style="left:511px">
      <li><svg width="6" height="8"><path d="M0 0l6 4-6 4z" fill="#f5893a"/></svg>Contact us</li>
      <li><svg width="6" height="8"><path d="M0 0l6 4-6 4z" fill="#f5893a"/></svg>Why choose WillowBend</li>
      <li><svg width="6" height="8"><path d="M0 0l6 4-6 4z" fill="#f5893a"/></svg>What clients say....</li>
      <li>Book now</li>
    </ul>
    <ul style="left:713px;top:63px">
      <li><svg width="6" height="8"><path d="M0 0l6 4-6 4z" fill="#f5893a"/></svg>Request a brochure</li>
      <li><svg width="6" height="8"><path d="M0 0l6 4-6 4z" fill="#f5893a"/></svg>FREE WillowBend Magazine</li>
    </ul>
  </footer>

  <div class="seo-band">
    Health Retreat &nbsp;|&nbsp; Fitness Holidays &nbsp;|&nbsp; Health Retreats &nbsp;|&nbsp; Fitness Camps &nbsp;|&nbsp; Health Retreats NSW &nbsp;|&nbsp; Weight Loss Retreats &nbsp;|&nbsp; Health Retreats Sydney<br>
    Retreat fitness &nbsp;|&nbsp; Health Retreats NSW &nbsp;|&nbsp; Weight Loss Retreat
  </div>

  <div class="legal">
    <div class="left">Contact Us &nbsp;|&nbsp; Book Now</div>
    <div class="right">© 2011 WillowBend Wellbeing PTY LTD | ABN 48201557930<br>Website Design - Website Development &amp; Search Engine Optimisation by Northgate Digital</div>
  </div>
</div>
</body>
</html>
```